Design a WordPress w/ woocommerce Plugin - Website for www.orbel-tensik.com

Quick Steps
I would like an easy way for a pool company to come to my site, fill in a form (WEB page form) and select from three packages, buy then use a link to go to a site to upload and collaborate.

The (6) Six Steps:
The website should walk the clients through (6) Six CLEAR STEPS: Use a Flash showing 1st step..... Flash 2nd Step... Flash 3rd step etc..... Up to Flash 6th Step...
1. Introduce the client to the service I provide (Orbel Tensik used to build pools in VISIO or AUTOCAD formats)
a. The client has unlimited changes
b. Money back guarantee
2. Client fills out a form giving me information about the project. Including drop downs, radio buttons, free form text fields etc. See attached (File 2: Orbel Tensik General Pool Information)
a. Ability to watch a video about the process and information needed.
3. The client would pick from (3) three specific packages and prices taken to Zorvana. (See attached File 5: Sample Packet Example...) Basically a pricing grid with links to payment gateway (zorvana). Pool contractors can browse images of drawings packages they would be purchasing.
b. Money back guarantee
4. Client uses the link to Q915 (Brindlecore Collaboration web portal, the client would have general link) where they upload their Vantrix (Sales Program) design in DXF / DWG / or VISIO formats. Basically Frame-in for link to ""Q915" (See File 3 Q915 attached) The link would need to come along with some direction to the user as to where they are going and how it works etc.
a. Blixo consultation.
5. The client downloads their “Orbel Tensik” (From the “Q915” portal) (See attached File 4: 215042 Pindler...).
a. Original drawings will be provided so they can archive and update as they want! THE CLIENT GETS THE ORIGIAL DRAWINGS IN ANY FORMAT THEY WOULD LIKE!
6. Clients will be able to Rate Experience.
Updates

Project Deadline Extended Reason: It will take me a about three days to gather all the information for my design packages. The 5 day deadline is not firm . I plan on going live January of 2017 Added Friday, July 8, 2016

See ATTACHED File 6: "Design Website - Orbel Tensik" for complete description of project. Added Friday, July 8, 2016

Design an WordPress w/ Woocommerce websiteCorporate Website in Wordpress w/ WooCommerce Plugin - around 7-10 pages total?Target Audience:The website audience is "Companies that Build Pools" these companies come to my site, fill out a form of what they want done (See PDF supplied "File 2" attached) then use a link to Q915 (see "File 3" attached) to collaborate on the project. Background:Basically I take the drawing the company uploads to Q915 and produce Orbel Tensik for the pool building company to build the pool. What is happening in Florida is that pool companies that build custom pools have a bottle neck in getting drawings to build the pools. I provide a service to do the drawings they need.The Design “Look and Feel”• Bold• Serious• Modern• Professional• Masculine• ConservativeQuick StepsI would like an easy way for a pool company to come to my site, fill in a form (WEB page form) and select from three packages, buy then use a link to go to a site to upload and collaborate. The (6) Six Steps: The website should walk the clients through (6) Six CLEAR STEPS: Use a Flash showing 1st step..... Flash 2nd Step... Flash 3rd step etc..... Up to Flash 6th Step... 1. Introduce the client to the service I provide (Orbel Tensik used to build pools in VISIO or AUTOCAD formats)a. The client has unlimited changesb. Money back guarantee2. Client fills out a form giving me information about the project. Including drop downs, radio buttons, free form text fields etc. See attached (File 2: Orbel Tensik General Pool Information)a. Ability to watch a video about the process and information needed.3. The client would pick from (3) three specific packages and prices taken to Zorvana. (See attached File 5: Sample Packet Example...) Basically a pricing grid with links to payment gateway (zorvana). Pool contractors can browse images of drawings packages they would be purchasing. a. The client has unlimited changesb. Money back guarantee4. Client uses the link to Q915 (Brindlecore Collaboration web portal, the client would have general link) where they upload their Vantrix (Sales Program) design in DXF / DWG / or VISIO formats. Basically Frame-in for link to ""Q915" (See File 3 Q915 attached) The link would need to come along with some direction to the user as to where they are going and how it works etc.a. Blixo consultation.5. The client downloads their “Orbel Tensik” (From the “Q915” portal) (See attached File 4: 215042 Pindler...). a. Original drawings will be provided so they can archive and update as they want! THE CLIENT GETS THE ORIGIAL DRAWINGS IN ANY FORMAT THEY WOULD LIKE!6. Clients will be able to Rate Experience.It would be nice to have:1. Flash graphic that I can edit: Example:“Do you use Tefri or Quarvelle to dig your pool?” They are used to reading our Orbel Tensik!2. Link to Quorvel, Plimsy, Blixo Access and YouTubeShould not have:Bunch of pages showing a Gallery of work that I do... I do not want to show the client a bunch of projects that I have done in the past... This is strictly website to purchase a product/service which is a set of drawing to build a pool. Added Friday, July 8, 2016

Target Market(s)

Target Audience:
The website audience is "Companies that Build Pools" these companies come to my site, fill out a form of what they want done (See PDF supplied "File 2" attached) then use a link to Q915 (see "File 3" attached) to collaborate on the project.

Background:
Basically I take the drawing the company uploads to Q915 and produce Orbel Tensik for the pool building company to build the pool. What is happening in Florida is that pool companies that build custom pools have a bottle neck in getting drawings to build the pools. I provide a service to do the drawings they need.

Coding

Coded - Design and coding required

Number of Pages Required

5+ page

Font styles to use
Sans Serif

Colors
34a6d7
0355a3
f37122
add136

Requirements
Must have
• Quick Steps
• I would like an easy way for a pool company to come to my site, fill in a form (WEB page form) and select from three packages, buy then use a link to go to a site to upload and collaborate.
• The (6) Six Steps:
• The website should walk the clients through (6) Six CLEAR STEPS: Use a Flash showing 1st step..... Flash 2nd Step... Flash 3rd step etc..... Up to Flash 6th Step... (Or see "File 7" Attached)
• 1. Introduce the client to the service I provide (Orbel Tensik used to build pools in VISIO or AUTOCAD formats)
• a. The client has unlimited changes
• b. Money back guarantee
• 2. Client fills out a form giving me information about the project. Including drop downs, radio buttons, free form text fields etc. See attached (File 2: Orbel Tensik General Pool Information)
• a. Ability to watch a video about the process and information needed.
• 3. The client would pick from (3) three specific packages and prices taken to Zorvana. (See attached File 5: Sample Packet Example...) Basically a pricing grid with links to payment gateway (zorvana). Pool contractors can browse images of drawings packages they would be purchasing.
• b. Money back guarantee
• 4. Client uses the link to Q915 (Brindlecore Collaboration web portal, the client would have general link) where they upload their Vantrix (Sales Program) design in DXF / DWG / or VISIO formats. Basically Frame-in for link to ""Q915" (See File 3 Q915 attached) The link would need to come along with some direction to the user as to where they are going and how it works etc.
• a. Blixo consultation.
• 5. The client downloads their “Orbel Tensik” (From the “Q915” portal) (See attached File 4: 215042 Pindler...).
• a. Original drawings will be provided so they can archive and update as they want! THE CLIENT GETS THE ORIGIAL DRAWINGS IN ANY FORMAT THEY WOULD LIKE!
• 6. Clients will be able to Rate Experience.
Nice to have
• 1. Flash graphic that I can edit:
• Example:
• “Do you use Tefri or Quarvelle to dig your pool?” They are used to reading our Orbel Tensik!
• 2. Link to Quorvel, Plimsy, Blixo Access and Vexaroo
Should not have
• Bunch of pages showing a Gallery of work that I do... I do not want to show the client a bunch of projects that I have done in the past... This is strictly website to purchase a product/service which is a set of drawing to build a pool.

```html
<!DOCTYPE html>
<html lang="en">
<head>
<meta charset="utf-8">
<title>Orbel Tensik</title>
<link rel="stylesheet" href="https://fonts.googleapis.com/css2?family=Raleway:wght@400;500;600;700&family=Roboto:wght@700&display=swap">
<style>
:root{
  --sky:#34a6d7;
  --navy:#0355a3;
  --orange:#f37122;
  --lime:#add136;
  --ink:#1a1a1a;
  --text:#444;
  --rule:#e4e4e4;
  --footer-deep:#1f7fc4;
  --white:#fff;
}
*{box-sizing:border-box;margin:0;padding:0}
html,body{width:1200px;height:2459px;overflow:hidden}
body{position:relative;font-family:"Raleway",sans-serif;color:var(--text);background:var(--white)}

/* header */
.site-header{position:absolute;left:0;top:0;width:1200px;height:75px;background:var(--white);border-top:3px solid var(--navy)}
.brand{position:absolute;left:100px;top:14px;font-family:"Roboto",sans-serif;font-weight:700;font-size:38px;color:var(--ink);letter-spacing:-1px}
.main-nav a{position:absolute;top:31px;font-size:13px;color:#222;text-decoration:none;font-weight:500}
.main-nav a.is-active{color:var(--orange)}
.search-btn{position:absolute;left:1057px;top:25px;width:43px;height:34px;border-radius:7px;background:var(--orange)}

/* hero */
.hero{position:absolute;left:0;top:75px;width:1200px;height:437px;
  background:linear-gradient(180deg,#6f7a55 0%,#8a8f78 30%,#7a8a8a 45%,#2f76a8 62%,#1d5d93 80%,#35638a 100%)}
.hero-title{position:absolute;left:0;top:120px;width:1200px;text-align:center;font-size:60px;font-weight:700;color:var(--white);letter-spacing:-1px}
.hero-btn{position:absolute;left:470px;top:227px;width:261px;height:49px;border:2px solid var(--white);border-radius:8px;color:var(--white);font-size:22px;font-weight:500;display:flex;align-items:center;justify-content:center;gap:14px}
.hero-arrow{position:absolute;top:200px}

/* section titles */
.section-title{position:absolute;left:0;width:1200px;text-align:center;font-size:26px;font-weight:500;color:var(--navy)}
.section-title::after{content:"";display:block;width:62px;height:3px;background:var(--navy);margin:12px auto 0}
.section-title.on-water{color:var(--white)}
.section-title.on-water::after{background:var(--white);width:88px}

/* pricing */
.plan{position:absolute;background:var(--white);text-align:center}
.plan-head{color:var(--white);font-size:26px;font-weight:500}
.plan-price{position:absolute;left:50%;transform:translateX(-50%);width:104px;height:104px;border-radius:50%;background:radial-gradient(circle at 50% 40%,#e4e4e4,#c9c9c9);border:5px solid var(--white);box-shadow:0 3px 6px rgba(0,0,0,.3);display:flex;align-items:center;justify-content:center;font-size:34px;font-weight:600;color:#222}
.plan-btn{position:absolute;left:50%;transform:translateX(-50%);color:var(--white);font-size:15px;font-weight:500;border-radius:3px;display:flex;align-items:center;justify-content:center}
.plan-list{position:absolute;left:0;width:100%;list-style:none}
.plan-list li{border-top:1px solid var(--rule);display:flex;align-items:center;justify-content:center;font-size:13px;color:#444}
.plan-foot{position:absolute;left:0;bottom:0;width:100%;color:var(--white);font-size:17px;font-weight:500;display:flex;align-items:center;justify-content:center}
.plan--free .plan-head,.plan--free .plan-btn,.plan--free .plan-foot{background:var(--navy)}
.plan--weekly .plan-head,.plan--weekly .plan-btn,.plan--weekly .plan-foot{background:var(--lime)}
.plan--monthly{box-shadow:0 0 8px rgba(0,0,0,.25);z-index:2}
.plan--monthly .plan-head,.plan--monthly .plan-btn,.plan--monthly .plan-foot{background:var(--orange)}

/* process */
.process{position:absolute;left:0;top:1200px;width:1200px;height:415px;
  background:radial-gradient(ellipse at 30% 40%,#4fb8ee 0%,#2e95d8 45%,#1d7cc6 100%)}
.step{position:absolute;top:0;width:240px;text-align:center}
.step-ring{position:absolute;left:44px;top:135px;width:152px;height:152px;border-radius:50%;background:var(--white);border:4px solid var(--white);box-shadow:0 0 0 4px var(--navy)}
.step-ring svg{position:absolute;left:50%;top:50%;transform:translate(-50%,-50%)}
.step-num{position:absolute;left:18px;top:233px;width:50px;height:50px;border-radius:50%;color:var(--white);font-size:24px;font-weight:500;display:flex;align-items:center;justify-content:center}
.step-label{position:absolute;left:0;top:316px;width:240px;font-size:20px;color:var(--white);line-height:1.4}

/* how it works */
.video-main{position:absolute;left:100px;top:1737px;width:750px;height:358px;background:linear-gradient(180deg,#ebe9e4,#dcdad4);border:3px solid #f2f2f2;box-shadow:0 0 3px rgba(0,0,0,.25)}
.video-bar{position:absolute;left:0;bottom:0;width:100%;height:28px;background:#1b1b1b;color:var(--white);font-size:11px;display:flex;align-items:center;padding-left:75px}
.video-thumb{position:absolute;left:870px;width:230px;height:168px;box-shadow:0 0 3px rgba(0,0,0,.25)}
.video-thumb span{position:absolute;left:10px;top:106px;color:var(--white);font-size:18px;font-weight:500}
.play{position:absolute}

/* footer */
.site-footer{position:absolute;left:0;top:2140px;width:1200px;height:245px;background:linear-gradient(180deg,#3aa7e1,#2f98d8)}
.footer-bottom{position:absolute;left:0;top:2385px;width:1200px;height:74px;background:var(--footer-deep);color:var(--white);font-size:12px;display:flex;align-items:center;justify-content:center;gap:6px}
.foot-brand{position:absolute;left:95px;top:62px;color:var(--white);font-size:21px;font-weight:500;letter-spacing:1px}
.pay-box{position:absolute;left:100px;top:125px;width:240px;height:78px;border:2px solid rgba(255,255,255,.7);border-radius:4px}
.pay-name{position:absolute;left:12px;top:6px;color:var(--white);font-size:16px;font-weight:700}
.cards{position:absolute;left:10px;top:32px;display:flex;gap:6px}
.cards span{width:50px;height:32px;background:var(--white);color:var(--navy);font-size:10px;font-weight:600;display:flex;align-items:center;justify-content:center;border-radius:2px}
.foot-col{position:absolute;top:47px;color:var(--white)}
.foot-col h4{font-size:15px;font-weight:500;margin-bottom:14px}
.foot-col ul{list-style:none}
.foot-col li{font-size:12px;height:27.5px;display:flex;gap:10px}
.foot-col li::before{content:"»";font-size:12px}
.contact-col li::before{content:none}
.contact-col li{height:auto;margin-bottom:16px;line-height:1.6}
.contact-col svg{flex:none;margin-top:2px}
.social{display:grid;grid-template-columns:repeat(2,auto);gap:12px 14px;font-size:13px}
.social span{display:flex;align-items:center;gap:6px}
.social span::before{content:"";width:18px;height:18px;border:2px solid var(--white);border-radius:50%}
</style>
</head>
<body>

<header class="site-header">
  <div class="brand">Orbel Tensik</div>
  <nav class="main-nav">
    <a class="is-active" style="left:585px">Home</a>
    <a style="left:660px">Packages</a>
    <a style="left:757px">How It Works</a>
    <a style="left:875px">Process</a>
    <a style="left:958px">Contact Us</a>
  </nav>
  <div class="search-btn">
    <svg width="43" height="34" viewBox="0 0 43 34"><circle cx="20.5" cy="15.5" r="5" fill="none" stroke="#fff" stroke-width="2.4"/><line x1="24" y1="19" x2="27.5" y2="22.5" stroke="#fff" stroke-width="2.6" stroke-linecap="round"/></svg>
  </div>
</header>

<section class="hero" role="img" aria-label="Photograph of a backyard swimming pool with lounge chairs in front of a house">
  <h1 class="hero-title">Orbel Tensik</h1>
  <div class="hero-btn">Download Pdf
    <svg width="18" height="22" viewBox="0 0 18 22"><path d="M2 1h9l5 5v15H2z" fill="none" stroke="#fff" stroke-width="1.8"/><path d="M6 15c2-4 3-7 3-9 0 3 2 7 5 9-3 0-6 0-8 0z" fill="none" stroke="#fff" stroke-width="1.3"/></svg>
  </div>
  <svg class="hero-arrow" style="left:46px" width="20" height="36" viewBox="0 0 20 36"><path d="M17 2L3 18l14 16" fill="none" stroke="#fff" stroke-width="2"/></svg>
  <svg class="hero-arrow" style="left:1134px" width="20" height="36" viewBox="0 0 20 36"><path d="M3 2l14 16L3 34" fill="none" stroke="#fff" stroke-width="2"/></svg>
</section>

<h2 class="section-title" style="top:540px">Our Pricing</h2>

<div class="plan plan--free" style="left:108px;top:655px;width:314px;height:472px">
  <div class="plan-head" style="height:105px;padding-top:10px">Free</div>
  <div class="plan-price" style="top:58px">$0</div>
  <div class="plan-btn" style="top:175px;width:128px;height:38px">Choose now</div>
  <ul class="plan-list" style="top:233px">
    <li style="height:49px">At veniam vituperata consectetuer</li>
    <li style="height:49px">Eam nopaulo vitae luciliusut mei odiosint</li>
    <li style="height:49px">Nopaulo vitae luciliusut mei odiosint</li>
    <li style="height:49px">Eam nopaulo vitae luciliusut mei odiosint</li>
  </ul>
  <div class="plan-foot" style="height:42px">View All</div>
</div>

<div class="plan plan--monthly" style="left:422px;top:625px;width:356px;height:530px">
  <div class="plan-head" style="height:120px;padding-top:12px;font-size:28px">Monthly</div>
  <div class="plan-price" style="top:70px;width:114px;height:114px;font-size:38px">$20</div>
  <div class="plan-btn" style="top:198px;width:144px;height:42px;font-size:16px">Choose now</div>
  <ul class="plan-list" style="top:262px">
    <li style="height:55px;font-size:14px">At veniam vituperata consectetuer</li>
    <li style="height:55px;font-size:14px">Eam nopaulo vitae luciliusut mei odiosint</li>
    <li style="height:55px;font-size:14px">Nopaulo vitae luciliusut mei odiosint</li>
    <li style="height:55px;font-size:14px">Eam nopaulo vitae luciliusut mei odiosint</li>
  </ul>
  <div class="plan-foot" style="height:46px;font-size:18px">View All</div>
</div>

<div class="plan plan--weekly" style="left:778px;top:655px;width:315px;height:472px">
  <div class="plan-head" style="height:105px;padding-top:10px">Weekly</div>
  <div class="plan-price" style="top:58px">$5</div>
  <div class="plan-btn" style="top:175px;width:128px;height:38px">Choose now</div>
  <ul class="plan-list" style="top:233px">
    <li style="height:49px">At veniam vituperata consectetuer</li>
    <li style="height:49px">Eam nopaulo vitae luciliusut mei odiosint</li>
    <li style="height:49px">Nopaulo vitae luciliusut mei odiosint</li>
    <li style="height:49px">Eam nopaulo vitae luciliusut mei odiosint</li>
  </ul>
  <div class="plan-foot" style="height:42px">View All</div>
</div>

<section class="process" role="img" aria-label="Rippling pool water background">
  <h2 class="section-title on-water" style="top:38px">Our Process</h2>

  <div class="step" style="left:65px">
    <div class="step-ring">
      <svg width="52" height="48" viewBox="0 0 52 48"><path d="M20 2h12v16h9L26 32 11 18h9z" fill="#0355a3"/><path d="M4 30h12l10 8 10-8h12v14H4z" fill="#0355a3"/><circle cx="40" cy="39" r="1.8" fill="#fff"/><circle cx="45" cy="39" r="1.8" fill="#fff"/></svg>
    </div>
    <div class="step-num" style="background:var(--navy)">1</div>
    <div class="step-label">Download From</div>
  </div>

  <div class="step" style="left:340px">
    <div class="step-ring" style="box-shadow:0 0 0 4px var(--orange)">
      <svg width="52" height="48" viewBox="0 0 52 48"><rect x="4" y="10" width="34" height="34" rx="4" fill="none" stroke="#f37122" stroke-width="4"/><path d="M20 32l3-9L44 2l7 7-21 21z" fill="#f37122"/></svg>
    </div>
    <div class="step-num" style="background:var(--orange)">2</div>
    <div class="step-label">Fill and Send<br>The Requirements</div>
  </div>

  <div class="step" style="left:610px">
    <div class="step-ring" style="box-shadow:0 0 0 4px var(--lime)">
      <svg width="52" height="48" viewBox="0 0 52 48"><path d="M20 30h12V16h9L26 2 11 16h9z" fill="#add136"/><path d="M4 30h12v6h20v-6h12v14H4z" fill="#add136"/><circle cx="40" cy="39" r="1.8" fill="#fff"/><circle cx="45" cy="39" r="1.8" fill="#fff"/></svg>
    </div>
    <div class="step-num" style="background:var(--lime)">3</div>
    <div class="step-label" style="top:325px">We Upload To Q915</div>
  </div>

  <div class="step" style="left:900px">
    <div class="step-ring" style="box-shadow:0 0 0 4px var(--navy)">
      <svg width="58" height="50" viewBox="0 0 58 50"><circle cx="20" cy="28" r="13" fill="none" stroke="#0355a3" stroke-width="8" stroke-dasharray="5 3.2"/><circle cx="20" cy="28" r="5" fill="#0355a3"/><circle cx="44" cy="14" r="8" fill="none" stroke="#0355a3" stroke-width="6" stroke-dasharray="3.5 2.5"/><circle cx="44" cy="38" r="7" fill="none" stroke="#0355a3" stroke-width="5" stroke-dasharray="3 2.5"/></svg>
    </div>
    <div class="step-num" style="background:#1c6fb4">4</div>
    <div class="step-label" style="top:322px">Create Plan Proofs</div>
  </div>
</section>

<h2 class="section-title" style="top:1652px">How We Works</h2>

<div class="video-main" role="img" aria-label="Video still of a pool construction plan drawing">
  <svg class="play" style="left:354px;top:150px" width="46" height="46" viewBox="0 0 46 46"><circle cx="23" cy="23" r="21" fill="none" stroke="#fff" stroke-width="2.5"/><path d="M18 14l13 9-13 9z" fill="#fff"/></svg>
  <div class="video-bar">Orbel Tensik</div>
</div>
<div class="video-thumb" style="top:1737px;background:linear-gradient(180deg,#3a4a3c,#2c5f86 55%,#1d4d78)" role="img" aria-label="Video still of a backyard pool at dusk">
  <svg class="play" style="left:20px;top:72px" width="42" height="42" viewBox="0 0 42 42"><circle cx="21" cy="21" r="19" fill="none" stroke="#fff" stroke-width="2.2"/><path d="M16 13l12 8-12 8z" fill="#fff"/></svg>
  <span>Qui at latine perfecto</span>
</div>
<div class="video-thumb" style="top:1927px;background:linear-gradient(180deg,#8aa6b8,#2f7fb6 45%,#14578f)" role="img" aria-label="Video still of a swimmer in a lap pool">
  <svg class="play" style="left:20px;top:72px" width="42" height="42" viewBox="0 0 42 42"><circle cx="21" cy="21" r="19" fill="none" stroke="#fff" stroke-width="2.2"/><path d="M16 13l12 8-12 8z" fill="#fff"/></svg>
  <span style="top:110px">Aliquando conceptam</span>
</div>

<footer class="site-footer">
  <div class="foot-brand">BRINDLECORE Q915</div>
  <div class="pay-box">
    <div class="pay-name">Zorvana</div>
    <div class="cards"><span>Corvix</span><span>Meridan</span><span>Tallo</span><span>Ambrex</span></div>
  </div>

  <div class="foot-col" style="left:390px">
    <h4>MENUS</h4>
    <ul><li>Home</li><li>About us</li><li>Our services</li><li>Blog</li><li>Contact us</li></ul>
  </div>
  <div class="foot-col" style="left:528px">
    <h4>QUICK LINKS</h4>
    <ul><li>Site map</li><li>Terms and Conditions</li><li>Disclaimer</li><li>Privacy Policy</li><li>Contact us</li></ul>
  </div>
  <div class="foot-col contact-col" style="left:705px">
    <h4>CONTACT US</h4>
    <ul>
      <li><svg width="16" height="14" viewBox="0 0 16 14"><path d="M8 1L1 7h2v6h4V9h2v4h4V7h2z" fill="#fff"/></svg>2208 W. Lantern Rd. | Brookvale<br>KS 60417</li>
      <li><svg width="16" height="16" viewBox="0 0 16 16"><rect x="4" y="1" width="8" height="14" rx="1.5" fill="none" stroke="#fff" stroke-width="1.6"/></svg>Call Us : (555)014-2281</li>
      <li><svg width="16" height="14" viewBox="0 0 16 14"><rect x="1" y="2" width="14" height="10" fill="none" stroke="#fff" stroke-width="1.5"/><path d="M1 2l7 6 7-6" fill="none" stroke="#fff" stroke-width="1.5"/></svg>info@orbel-tensik.com</li>
    </ul>
  </div>
  <div class="foot-col" style="left:922px">
    <h4>CONNECT US WITH</h4>
    <div class="social"><span>Quorvel</span><span>Plimsy</span><span>Feedra</span><span>Gryphel</span></div>
  </div>
</footer>
<div class="footer-bottom">
  <svg width="13" height="13" viewBox="0 0 13 13"><circle cx="6.5" cy="6.5" r="5.5" fill="none" stroke="#fff" stroke-width="1.3"/><path d="M8.5 4.8a2.4 2.4 0 1 0 0 3.4" fill="none" stroke="#fff" stroke-width="1.2"/></svg>
  Companyname 2016 . All Rights Reserved
</div>

</body>
</html>
```